Create a billboard for my cafe : Le coin sucré (Not a menu but a Billboard)

We are launching a visual campaign for 'Le coin sucré,' a café that epitomizes the pleasure of taking a delightful break. The campaign will feature images to be displayed on digital screens and freestanding posters within a shopping center. We require images that capture the essence of a cozy, inviting café atmosphere. The imagery should include visually appealing representations of our products—coffee, pastries, donuts, sandwiches, waffles, crepes, fruit juices, and smoothies. The design should evoke a sense of warmth and welcome, enticing shoppers to visit our café for a relaxing break. The aesthetic should be clean and modern, yet convey the richness and variety of our menu. Colors should be harmonious and soothing, with a focus on food appeal and comfort. These images will play a crucial role in attracting a diverse audience, creating a visual connection between the shoppers and the delightful experience our café offers.

Target Market(s)

Our shop opens in a high end mall. The demography of the Customers is on average 45 years with a lot of seniors.

Industry/Entity Type

Cafe

Requirements
Must have
• The text should be in french. This is a suggestion you can use : Offrez-vous un moment, goûtez nos douceurs ! Le coin sucré Ouvert bientôt!

```html
<!DOCTYPE html>
<html lang="fr">
<head>
<meta charset="utf-8">
<title>Le coin sucré — Ouvert bientôt</title>
<link rel="stylesheet" href="https://fonts.googleapis.com/css2?family=Montserrat:wght@600;700;800;900&display=swap">
<style>
  :root {
    --page-bg: #dde5ea;
    --wine-dark: #2a0000;
    --wine: #8e0000;
    --red-bright: #e3240f;
    --red-deep: #a82528;
    --red-soft: #c33a34;
    --gold: #e7cc58;
    --gold-deep: #c9a93a;
    --yellow: #ffe600;
    --white: #ffffff;
    --ink: #000000;
  }
  html, body {
    margin: 0;
    padding: 0;
    width: 1200px;
    height: 1088px;
    overflow: hidden;
    background: var(--page-bg);
    font-family: "Montserrat", Arial, sans-serif;
  }
  .billboard {
    position: absolute;
    left: 40px;
    top: 264px;
    width: 1120px;
    height: 560px;
    overflow: hidden;
    box-shadow: 0 10px 30px rgba(0,0,0,.25);
  }
  .billboard-art {
    position: absolute;
    inset: 0;
    width: 1120px;
    height: 560px;
  }
  .brand {
    position: absolute;
    left: 60px;
    top: 26px;
    display: flex;
    align-items: center;
    gap: 10px;
    color: var(--gold);
    font-weight: 700;
    font-size: 28px;
    letter-spacing: .5px;
  }
  .brand-dot {
    width: 16px;
    height: 16px;
    border-radius: 50%;
    background: var(--gold);
  }
  .headline {
    position: absolute;
    color: var(--white);
    line-height: 1;
    margin: 0;
  }
  .headline-left { left: 30px; top: 170px; }
  .headline-right { right: 60px; top: 70px; text-align: right; }
  .headline .caps {
    display: block;
    font-weight: 600;
    font-size: 38px;
    letter-spacing: 1px;
    text-transform: uppercase;
  }
  .headline .lower {
    display: block;
    font-weight: 800;
    font-size: 56px;
    margin-top: 6px;
  }
  .launch-line {
    position: absolute;
    left: 30px;
    bottom: 22px;
    margin: 0;
    font-weight: 800;
    font-size: 60px;
    line-height: 1;
    white-space: nowrap;
  }
  .launch-name { color: var(--yellow); font-weight: 800; }
  .launch-status {
    color: var(--white);
    font-weight: 900;
    margin-left: 14px;
    text-shadow: 3px 3px 2px rgba(0,0,0,.55);
  }
</style>
</head>
<body>
<div class="billboard">
  <svg class="billboard-art" viewBox="0 0 1120 560" xmlns="http://www.w3.org/2000/svg" aria-hidden="false">
    <defs>
      <linearGradient id="wineGrad" x1="0" y1="0" x2="1" y2="0">
        <stop offset="0" stop-color="var(--wine-dark)"/>
        <stop offset="1" stop-color="#a30000"/>
      </linearGradient>
      <linearGradient id="redGrad" x1="0" y1="1" x2="1" y2="0">
        <stop offset="0" stop-color="var(--red-bright)"/>
        <stop offset=".6" stop-color="#c4281c"/>
        <stop offset="1" stop-color="var(--red-deep)"/>
      </linearGradient>
      <linearGradient id="bottomGrad" x1="0" y1="0" x2="1" y2="0">
        <stop offset="0" stop-color="var(--red-soft)"/>
        <stop offset=".45" stop-color="#e0391f"/>
        <stop offset="1" stop-color="var(--red-deep)"/>
      </linearGradient>
      <linearGradient id="goldGrad" x1="0" y1="0" x2="1" y2="0">
        <stop offset="0" stop-color="var(--gold-deep)"/>
        <stop offset=".5" stop-color="#f6e48a"/>
        <stop offset="1" stop-color="var(--gold)"/>
      </linearGradient>
      <linearGradient id="photoEggs" x1="0" y1="0" x2="1" y2="1">
        <stop offset="0" stop-color="#f2b431"/><stop offset=".5" stop-color="#f3ead2"/><stop offset="1" stop-color="#5b6b2c"/>
      </linearGradient>
      <linearGradient id="photoSmoothie" x1="0" y1="0" x2="0" y2="1">
        <stop offset="0" stop-color="#f07a86"/><stop offset="1" stop-color="#b5654a"/>
      </linearGradient>
      <linearGradient id="photoPastry" x1="0" y1="0" x2="1" y2="1">
        <stop offset="0" stop-color="#f0b458"/><stop offset="1" stop-color="#c76a1c"/>
      </linearGradient>
      <linearGradient id="photoCoffee" x1="0" y1="0" x2="1" y2="1">
        <stop offset="0" stop-color="#e9e6e2"/><stop offset="1" stop-color="#b5aea6"/>
      </linearGradient>
      <clipPath id="photoBand">
        <path d="M120,436 C300,346 500,316 700,316 C900,316 1000,266 1120,216 L1120,344 C950,394 800,428 600,418 C400,408 200,430 0,494 Z"/>
      </clipPath>
    </defs>

    <rect class="field-red" width="1120" height="560" fill="url(#redGrad)"/>
    <polygon class="field-wine" points="0,0 900,0 0,470" fill="url(#wineGrad)"/>
    <polygon class="diagonal-stripe" points="900,0 950,0 30,480 0,486 0,470" fill="var(--ink)"/>
    <polygon class="sheen" points="1000,0 1060,0 700,300 640,300" fill="#ffffff" opacity=".05"/>

    <g clip-path="url(#photoBand)">
      <polygon role="img" aria-label="Photo de toasts à l'avocat et œufs mollets" points="0,200 470,200 360,560 0,560" fill="url(#photoEggs)"/>
      <polygon role="img" aria-label="Photo d'un smoothie à la fraise" points="470,200 720,200 620,560 360,560" fill="url(#photoSmoothie)"/>
      <polygon role="img" aria-label="Photo d'une viennoiserie dorée sur assiette" points="720,200 940,200 840,560 620,560" fill="url(#photoPastry)"/>
      <polygon role="img" aria-label="Photo d'une tasse de café en cours de remplissage" points="940,200 1120,200 1120,560 840,560" fill="url(#photoCoffee)"/>
    </g>

    <path class="gold-band-top" d="M100,446 C290,346 500,304 700,304 C900,304 1000,254 1120,200 L1120,216 C1000,266 900,316 700,316 C500,316 300,346 120,436 Z" fill="url(#goldGrad)"/>
    <path class="bottom-field" d="M0,494 C200,430 400,408 600,418 C800,428 950,394 1120,344 L1120,560 L0,560 Z" fill="url(#bottomGrad)"/>
    <path class="gold-band-bottom" d="M0,494 C200,430 400,408 600,418 C800,428 950,394 1120,344 L1120,362 C950,412 800,446 600,436 C400,426 200,446 0,512 Z" fill="url(#goldGrad)"/>
  </svg>

  <div class="brand"><span class="brand-dot"></span>Le coin sucré</div>

  <h2 class="headline headline-left">
    <span class="caps">Offrez-vous</span>
    <span class="lower">un moment</span>
  </h2>

  <h2 class="headline headline-right">
    <span class="caps">Goûtez</span>
    <span class="lower">nos douceurs !</span>
  </h2>

  <p class="launch-line"><span class="launch-name">Le coin sucré</span><span class="launch-status">OUVERT BIENTÔT!</span></p>
</div>
</body>
</html>
```